corVenna Bright Studio Website coded

New website (coded) promoting photography, videography and graphic design
Fresh, clean, crisp modern striking
easy to navigate
www.corvenna.com.au, current outdated site. Needs to be more streamlined.
Check out www.facebook.com/corVenna.Snaps
Offering the following photography categories
Family portraiture
Lifestyle photography (celebrations)
Pets
Fine Art
Arts and Sports .. I.e. Bands, schools, teams, performances, etc)
Commercial
Additional Services
Design
Photo books
Photo restoration
Videography and editing
Then there should be a bio, testimonial, where I am located, FAQ, pricing info perhaps all under the one umbrella of About Me or INFO
I also need a client log-in area to sell my photography, i.e. a plug-in. I am currently using pictavault for this.

```html
<!DOCTYPE html>
<html lang="en">
<head>
<meta charset="utf-8">
<title>corVenna Bright Studio</title>
<link rel="stylesheet" href="https://fonts.googleapis.com/css2?family=Source+Sans+3:wght@400;600;700&family=Oswald:wght@500;700&display=swap">
<style>
:root{
  --ink:#1b1b1b;
  --orange:#ec7424;
  --lime:#a3c93a;
  --lime-dark:#8db52d;
  --red:#c21f2c;
  --red-dark:#9c1420;
  --yellow:#f6b800;
  --purple:#a4479c;
  --white:#ffffff;
  --stripe:#e6e6e6;
  --rule:#d6d6d6;
  --muted:#cfcfcf;
  --text:#2a2a2a;
}
*{box-sizing:border-box;margin:0;padding:0}
html,body{width:1200px;height:1001px;overflow:hidden;background:var(--white)}
body{position:relative;font-family:"Source Sans 3",Arial,sans-serif;color:var(--text)}
.abs{position:absolute}
.cond{font-family:"Oswald","Arial Narrow",sans-serif}

.site-header{left:0;top:0;width:1200px;height:113px;background:var(--ink)}
.header-stripe{left:0;top:116px;width:1200px;height:25px;background:var(--stripe)}
.brand{left:33px;top:0;width:330px;height:153px}
.brand-name{left:120px;top:22px;width:180px;text-align:center;font-size:42px;font-weight:400;color:var(--white);letter-spacing:-1px}

.search{left:629px;top:20px;width:248px;height:35px;background:var(--white);border:0}
.search-btn{left:877px;top:20px;width:35px;height:35px;background:var(--lime)}
.phone-icon{left:944px;top:20px}
.phone{left:977px;top:18px;font-size:25px;font-weight:600;color:var(--orange);letter-spacing:1.5px}

.main-nav{left:322px;top:78px;width:832px;display:flex;justify-content:space-between;font-size:15.5px;color:var(--white);white-space:nowrap}
.main-nav .active{color:var(--orange)}
.nav-marker{left:322px;top:113px;width:83px;height:3px;background:var(--orange)}
.nav-tick{left:354px;top:116px}

.hero{left:32px;top:160px;width:790px;height:464px;background:radial-gradient(ellipse at 50% 45%,#6b4a3a 0%,#2a1c16 28%,#0c0c0c 55%)}
.thumb{top:627px;height:133px}
.thumb-book{left:32px;width:262px;background:linear-gradient(135deg,#5a7890,#c9c2b6 60%,#8a8377)}
.thumb-baby{left:297px;width:262px;background:radial-gradient(ellipse at 50% 50%,#8c5e46 0%,#1a1210 45%,#0b0b0b 70%)}
.thumb-boat{left:561px;width:261px;background:linear-gradient(160deg,#3a3a3a,#9a9a9a 55%,#2c2c2c)}

.promo{left:825px;width:326px;color:var(--white);text-align:center;overflow:hidden}
.promo-login{top:160px;height:206px;background:var(--lime)}
.login-head{position:absolute;left:0;width:100%;top:16px;font-size:29px;line-height:35px;font-weight:600}
.login-band{position:absolute;left:0;top:91px;width:100%;height:56px;background:#000;color:var(--orange);font-size:36px;font-weight:700;line-height:56px;letter-spacing:.5px}
.login-order{position:absolute;left:0;top:147px;width:100%;height:59px;background:var(--lime-dark);color:#000;font-size:36px;font-weight:700;line-height:57px}

.promo-signup{top:373px;height:203px;background:linear-gradient(90deg,var(--red-dark),var(--red) 55%,#d2242f)}
.signup-now{position:absolute;right:25px;top:20px;font-size:28px;font-weight:600;color:var(--yellow)}
.signup-get{position:absolute;left:23px;top:58px;font-size:35px;font-weight:600}
.signup-arrow{position:absolute;left:43px;top:115px}
.signup-voucher{position:absolute;right:14px;top:115px;font-size:37px;font-weight:700;color:#000;line-height:52px}

.promo-offers{top:582px;height:178px;background:var(--purple)}
.offers-head{position:absolute;left:0;width:100%;top:12px;font-size:28px;font-weight:600;letter-spacing:1px}
.offers-num{position:absolute;left:72px;top:30px;font-size:108px;font-weight:700;line-height:120px}
.offers-pct{position:absolute;left:203px;top:44px;font-size:40px;font-weight:700}
.offers-off{position:absolute;left:192px;top:98px;font-size:42px;font-weight:700}
.offers-note{position:absolute;left:0;width:100%;top:155px;font-size:12.5px;font-weight:700;color:#1a1a1a}

.rule{left:32px;top:768px;width:1119px;height:1px;background:var(--rule)}
.news-label{left:32px;top:789px;font-size:16px;font-weight:700;color:var(--ink);letter-spacing:.3px}
.news-input{left:240px;top:785px;width:225px;height:31px;border:1px solid #b8b8b8;font-size:13px;color:#888;padding:6px 13px}
.news-submit{left:477px;top:785px;width:82px;height:31px;background:var(--orange);color:var(--white);font-size:16px;font-weight:700;text-align:center;line-height:31px}
.quote{left:612px;top:786px;width:540px;text-align:center;font-size:16px;line-height:20px;color:var(--ink)}

.footer-stripe{left:0;top:850px;width:1200px;height:25px;background:var(--stripe)}
.site-footer{left:0;top:875px;width:1200px;height:126px;background:var(--ink)}
.foot-col{top:886px;color:var(--white)}
.foot-col h3{font-size:16px;font-weight:400;letter-spacing:.3px;margin-bottom:8px}
.foot-col li{list-style:none;font-size:13px;line-height:16.8px;color:var(--muted);letter-spacing:.3px}
.col-services{left:33px}
.col-extra{left:416px}
.contact-panel{left:775px;top:863px}
.contact{left:859px;color:var(--ink);font-size:15px;white-space:nowrap}
.join{top:896px}
.social{display:inline-flex;gap:6px;margin-left:8px;vertical-align:middle}
.social span{font-size:11px;font-weight:600;color:var(--white);background:var(--ink);padding:3px 5px;border-radius:3px}
.mail{top:927px}
.copy{top:954px;color:var(--white)}
</style>
</head>
<body>

<header>
  <div class="abs site-header"></div>
  <div class="abs header-stripe"></div>
  <svg class="abs brand" viewBox="0 0 330 153" aria-hidden="true"><polygon points="0,0 330,0 170,153" fill="#ec7424"/></svg>
  <div class="abs brand-name">corVenna</div>

  <div class="abs search" aria-label="Search"></div>
  <div class="abs search-btn">
    <svg width="35" height="35" viewBox="0 0 35 35" aria-hidden="true"><circle cx="15" cy="15" r="5.5" fill="none" stroke="#fff" stroke-width="3"/><line x1="19" y1="19" x2="26" y2="26" stroke="#fff" stroke-width="4" stroke-linecap="round"/></svg>
  </div>
  <svg class="abs phone-icon" width="24" height="32" viewBox="0 0 24 32" aria-hidden="true"><path d="M6 2 L11 2 L12 9 L8 11 C9 16 11 20 14 23 L18 20 L23 24 L21 30 C12 29 3 18 2 7 Z" fill="#ec7424"/></svg>
  <div class="abs phone">0491 570 156</div>

  <nav class="abs main-nav">
    <span class="active">ABOUT ME</span><span>|</span><span>WHAT I OFFER</span><span>|</span><span>GALLERY</span><span>|</span><span>INFO</span><span>|</span><span>NEWS</span><span>|</span><span>SPECIAL OFFERS</span><span>|</span><span>BLOG</span><span>|</span><span>CLIENT LOG IN</span><span>|</span><span>REGISTER</span>
  </nav>
  <div class="abs nav-marker"></div>
  <svg class="abs nav-tick" width="18" height="9" viewBox="0 0 18 9" aria-hidden="true"><polygon points="0,0 18,0 9,9" fill="#ec7424"/></svg>
</header>

<main>
  <div class="abs hero" role="img" aria-label="Studio portrait of a smiling baby held in an adult's hands against black"></div>
  <div class="abs thumb thumb-book" role="img" aria-label="Open photo book with family pictures"></div>
  <div class="abs thumb thumb-baby" role="img" aria-label="Baby portrait on black background"></div>
  <div class="abs thumb thumb-boat" role="img" aria-label="Black and white photo of a child with a toy boat at a pond"></div>

  <section class="abs promo promo-login">
    <div class="login-head">LOG IN<br>EXISTING CLIENT</div>
    <div class="login-band cond">TRACK YOUR</div>
    <div class="login-order cond">ORDER</div>
  </section>

  <section class="abs promo promo-signup">
    <div class="signup-now">SIGN UP NOW</div>
    <div class="signup-get">AND GET YOUR</div>
    <svg class="signup-arrow" width="283" height="52" viewBox="0 0 283 52" aria-hidden="true"><polygon points="0,0 283,0 283,52 0,52 24,26" fill="#f6b800"/></svg>
    <div class="signup-voucher cond">GIFT VOUCHER</div>
  </section>

  <section class="abs promo promo-offers">
    <div class="offers-head">SPECIAL&nbsp;&nbsp;OFFERS</div>
    <div class="offers-num cond">50</div>
    <div class="offers-pct cond">%</div>
    <div class="offers-off cond">OFF</div>
    <div class="offers-note">This Offers Is Valid For Limited Period</div>
  </section>

  <div class="abs rule"></div>
  <div class="abs news-label cond">SIGN UP FOR NEWSLETTER</div>
  <div class="abs news-input">Type Your Email</div>
  <div class="abs news-submit cond">SUBMIT</div>
  <p class="abs quote">“ I am privileged to be able to do what I love most: capturing a moment &amp; transforming it into an everlasting story.”</p>
</main>

<footer>
  <div class="abs footer-stripe"></div>
  <div class="abs site-footer"></div>
  <div class="abs foot-col col-services">
    <h3>SERVICES</h3>
    <ul><li>Family portraiture</li><li>Lifestyle photography (celebrations)</li><li>Pets</li><li>Fine Art</li></ul>
  </div>
  <div class="abs foot-col col-extra">
    <h3>ADDITIONAL&nbsp; SERVICES</h3>
    <ul><li>Design</li><li>Photo Books</li><li>Photo Restoration</li><li>Videography and Editing</li></ul>
  </div>
  <svg class="abs contact-panel" width="376" height="138" viewBox="0 0 376 138" aria-hidden="true"><polygon points="35,0 376,0 376,138 35,138 0,69" fill="#ec7424"/></svg>
  <div class="abs contact join">JOIN ME ON :<span class="social"><span>Kestrel</span><span>Lumen</span><span>Orbit</span><span>Nexa</span></span></div>
  <div class="abs contact mail">E-mail:&nbsp;&nbsp; hello@corvenna.com.au</div>
  <div class="abs contact copy">Copyright 2014 &nbsp;©&nbsp; corvenna.com.au</div>
</footer>

</body>
</html>
```